Game, Voice & Dedicated Server Company Needs a Business Card Design

We need a new business card design, centered around our new logo (PSD provided below).

Designs that we do like:
https://pixelmarsh.net/item/corporate-business-card/5382017?s_rank=43 (needs to be made more eye catching)

Our main areas of business are:
- Dedicated Servers
- Game Servers
- Voice Servers
- Mitigation Security Specialists

Industry/Entity Type

Business

Contact Information for Business Card

On the card: (and anything else you would suggest)
- Staff member name
- Staff member position in company
- Staff member phone number
- Staff member email
- Other / Staff member Skype
- Website link

Colors
9bcb3c
abd036

Requirements
Must have
• Design of Card:
• - Green (same green as the logo)
• - Business / Corporate design
• - Something a little different / abstract that shouts premium

```html
<!DOCTYPE html>
<html lang="en">
<head>
<meta charset="utf-8">
<title>Vantage Hosting – Business Card</title>
<link rel="stylesheet" href="https://fonts.googleapis.com/css2?family=Open+Sans:ital,wght@0,400;0,700;1,400&display=swap">
<style>
  :root {
    --page: #e4e2dd;
    --card: #0e0e0f;
    --card-sheen: #1c1c1e;
    --green: #9bcb3c;
    --green-soft: #abd036;
    --white: #f2f2f2;
    --grey: #bdbdbd;
  }
  * { box-sizing: border-box; margin: 0; padding: 0; }
  html, body {
    width: 1200px; height: 950px; overflow: hidden;
    background: var(--page);
    font-family: "Open Sans", Arial, sans-serif;
  }
  .canvas {
    width: 1200px; height: 950px;
    display: flex; flex-direction: column;
    align-items: center; justify-content: center; gap: 50px;
  }
  .card {
    position: relative;
    width: 700px; height: 400px;
    background: linear-gradient(120deg, var(--card-sheen) 0%, var(--card) 45%, var(--card) 100%);
    box-shadow: 0 10px 30px rgba(0,0,0,.25);
    overflow: hidden;
  }

  /* Contact side */
  .contact-card .brand-mark {
    position: absolute; top: 70px; left: 0; right: 0;
    display: flex; justify-content: center; align-items: center; gap: 12px;
  }
  .brand-square { width: 22px; height: 22px; background: var(--green); }
  .brand-name {
    color: var(--green); font-weight: 700; font-size: 26px;
    letter-spacing: 1px; text-transform: uppercase;
  }
  .rule {
    position: absolute; left: 90px; right: 90px; height: 1px;
    background: linear-gradient(90deg, transparent, var(--green) 30%, var(--green) 70%, transparent);
  }
  .rule-top { top: 160px; }
  .rule-bottom { top: 320px; }
  .contact-block {
    position: absolute; top: 185px; left: 0; right: 0;
    text-align: center; color: var(--white); font-size: 19px; line-height: 1.6;
  }
  .person-name { color: var(--green); font-weight: 700; font-size: 22px; }
  .person-role { color: var(--white); }
  .label { color: var(--green); }

  /* Brand side */
  .brand-card .brand-lockup {
    position: absolute; top: 110px; left: 90px;
    display: flex; align-items: center; gap: 16px;
  }
  .brand-card .brand-square { width: 40px; height: 40px; }
  .brand-card .brand-name { font-size: 48px; line-height: 1; }
  .services {
    position: absolute; top: 220px; left: 90px;
    color: var(--white); font-style: italic; font-size: 21px; line-height: 1.7;
  }
  .dot {
    display: inline-block; width: 8px; height: 8px; border-radius: 50%;
    background: var(--green); margin: 0 10px; vertical-align: middle;
  }
</style>
</head>
<body>
<main class="canvas">
  <section class="card contact-card" aria-label="Card contact side">
    <div class="brand-mark">
      <span class="brand-square"></span>
      <span class="brand-name">Vantage Hosting</span>
    </div>
    <div class="rule rule-top"></div>
    <div class="contact-block">
      <p><span class="person-name">DANIEL MARSH</span> <span class="person-role">&nbsp;-&nbsp; CEO/Founder</span></p>
      <p><span class="label">Phone:</span> 555 214 8830 &nbsp;<span class="label">Email:</span> name@vantagehost.net</p>
      <p><span class="label">Web:</span> vantagehost.net &nbsp;<span class="label">Skype:</span> vantagehost.net</p>
    </div>
    <div class="rule rule-bottom"></div>
  </section>

  <section class="card brand-card" aria-label="Card brand side">
    <div class="brand-lockup">
      <span class="brand-square"></span>
      <span class="brand-name">Vantage Hosting</span>
    </div>
    <div class="services">
      <p>Dedicated Servers<span class="dot"></span>Game Servers</p>
      <p>Voice Servers<span class="dot"></span>Business relations</p>
    </div>
  </section>
</main>
</body>
</html>
```